Defend science flier

Put my name and text below on one side of flier, and place other text on other side. Try to keep file about 4 by 6 or 6 by 8 inches.

Target Market(s)

Community and retailers.

Industry/Entity Type

Retail and concerned community.

Font styles to use
Serif

Requirements
Must have
• Good, eye-catching titles. Be smaller format. Not 8 by 11
Nice to have
• Black and white text. Maybe bullets etc for organizion but no decorations.
Should not have
• Any decoration

```html
<!DOCTYPE html>
<html lang="en">
<head>
<meta charset="utf-8">
<title>Defend Science Flier</title>
<link href="https://fonts.googleapis.com/css2?family=Poppins:ital,wght@0,300;0,400;0,700;1,300;1,400;1,700&display=swap" rel="stylesheet">
<style>
  :root {
    --backdrop: #e3e2e3;
    --paper: #ffffff;
    --ink: #000000;
  }
  * { box-sizing: border-box; margin: 0; padding: 0; }
  html, body {
    width: 953px; height: 1200px; overflow: hidden;
    background: var(--backdrop);
  }
  body { position: relative; font-family: "Poppins", sans-serif; color: var(--ink); }

  .card {
    position: absolute; width: 357px; height: 537px;
    background: var(--paper);
  }
  .card--sins { left: 97px; top: 46px; }
  .card--diversity { left: 527px; top: 195px; }
  .card--author { left: 146px; top: 617px; }

  .block { position: absolute; left: 36px; }

  .card-title { font-weight: 700; font-size: 20px; line-height: 24.5px; letter-spacing: -0.2px; width: 240px; }
  .lead { font-weight: 300; font-size: 19px; line-height: 24px; text-transform: uppercase; }
  .lead em { font-style: italic; font-weight: 300; }
  .lead--sins { width: 245px; }
  .lead--diversity { width: 282px; }
  .body-text { font-size: 12.4px; line-height: 15px; width: 258px; }
  .body-text p + p { margin-top: 15px; }

  .sin-list { list-style: none; width: 262px; }
  .sin-list li { display: flex; font-size: 12.4px; line-height: 15px; }
  .sin-list li + li { margin-top: 14.5px; }
  .sin-list .num { font-weight: 700; width: 28px; flex: none; }

  .signature { position: absolute; left: 37px; top: 493px; font-weight: 300; font-size: 14.5px; line-height: 18px; text-transform: uppercase; }

  .author-name { font-weight: 700; font-size: 17.5px; line-height: 21px; }
  .author-tag { font-weight: 700; font-style: italic; font-size: 17.5px; line-height: 21px; width: 270px; }
  .quote { font-style: italic; }
  .cta { font-weight: 700; }
</style>
</head>
<body>

<section class="card card--sins">
  <h1 class="block card-title" style="top:39px;">Why Did the Culture Change?</h1>
  <p class="block lead lead--sins" style="top:109px;">During the 1960s, we socialized the seven deadly sins. Therefore:</p>
  <ol class="block sin-list" style="top:224px;">
    <li><span class="num">1.</span><span>Pride became “Racism.”</span></li>
    <li><span class="num">2.</span><span>Lust became “Sexism” and “Gender” existing “out there.”</span></li>
    <li><span class="num">3.</span><span>Gluttony became “Consumer Fetishism.”</span></li>
    <li><span class="num">4.</span><span>Vanity became “Media Images of Beauty.”</span></li>
    <li><span class="num">5.</span><span>Sloth became The lack of social action: “Are you fighting for diversity?”</span></li>
  </ol>
  <p class="signature">Name Lastname</p>
</section>

<section class="card card--diversity">
  <h2 class="block lead lead--diversity" style="top:37px;">This <em>“Fight for Diversity”</em> inspires attacks against people like Dr. Hallbrenner for asserting any reality principle about human nature.</h2>
  <div class="block body-text" style="top:226px;">
    <p>These thugs are religious crusaders who ignore the rule of law and try to stop the progress of science. These fanatics go around and give people a “tear-test”—as during the Salem witch trials. Don’t let them take over.</p>
    <p>The educational and culture elites—such as Hollywood—now reject these theological “social sins.” The elites are replacing theology with traditional, human-based sin.</p>
  </div>
  <p class="signature">Name Lastname</p>
</section>

<section class="card card--author">
  <div class="block" style="top:37px;">
    <h2 class="author-name">Victor Hallbrenner, Ph.D.</h2>
    <p class="author-tag">“The Master Architect of Psychology and History.”</p>
  </div>
  <div class="block body-text" style="top:113px;">
    <p>Victor’s Bio-Psych has Restructured the Liberal Arts and Sciences—from Genetics to the Fine Arts and Hollywood.</p>
    <p>Museum Catalogues, Better Nonfiction, and Hollywood Films Now Use Victor’s Methods.</p>
    <p>Victor’s Biopsych is endorsed by Dr. R. Martin Ellery, professor of psychiatry at Northfield Medical School, who said:</p>
    <p class="quote">“Modern sleep and dream research teaches us—as does Victor Hallbrenner’s book Private Vice or Public Vice—that all human activities, including art and politics, are products of the human brain, and that each of us has the privilege and responsibility of using it and communicating its creations.”</p>
    <p class="cta">See Victor’s homepage for more details: www.victor-hallbrenner.org</p>
  </div>
  <p class="signature">Name Lastname</p>
</section>

</body>
</html>
```